Letter Head Design - Finance industry

Design a letterhead to match the logo. Needs to be clean, simple and crisp. I'm open to suggestions. Will be using the logo that was submitted last with the W crossed over

Target Market(s)

Small medium businesses and government department's

Industry/Entity Type

Industry

Font styles to use
Sans Serif

Colors
cadf82
bcd85c
acd036
9bcb3c
e9e9e9
aaaaaa
000000
7f7f7f
b7b7b7

Requirements
Must have
• Need to display: Logo, Business address, ABN number, ASIC register number, contact phone, website, company email. Details are as per below:

Suite 4B Level 17
Marlowe Crest House
9 Tindall Lane
Sydney NSW 2000
Landline Ph: 02 5193 4620
Ph: 1300 4719 55
Email: enquiries@coinharbourco.com.au
W: www.coinharbourco.com.au

On the footer, the details below need to be specified:
ABN: 47 381 950 623
ASIC Registration Number: 31 749218605

Should not have
• No imagery or design that is not in line with the logo

```html
<!DOCTYPE html>
<html lang="en">
<head>
<meta charset="utf-8">
<title>Coin Harbour Co – Letterhead</title>
<link rel="stylesheet" href="https://fonts.googleapis.com/css2?family=Arimo:wght@400;600&family=Open+Sans:wght@400&display=swap">
<style>
  :root {
    --backdrop: #3a3a3a;
    --sheet: #f6f7f7;
    --band-grey: #7f7f7f;
    --accent-green: #9bcb3c;
    --ink: #000000;
    --footer-ink: #ffffff;
    --signature-tone: #e9e9e9;
  }
  * { margin: 0; padding: 0; box-sizing: border-box; }
  html, body {
    width: 999px; height: 1200px; overflow: hidden;
    background: var(--backdrop);
  }
  .letterhead {
    position: absolute; left: 113px; top: 56px;
    width: 771px; height: 1088px;
    background: var(--sheet);
  }
  .top-band {
    position: absolute; left: 0; top: 0; width: 100%; height: 29px;
    background: var(--band-grey);
  }
  .brand {
    position: absolute; left: 44px; top: 76px;
    display: flex; align-items: center; gap: 8px;
    font-family: "Arimo", Arial, sans-serif;
    font-weight: 600; font-size: 27px; letter-spacing: -0.3px;
    color: var(--accent-green);
  }
  .brand-dot {
    width: 12px; height: 12px; border-radius: 50%;
    background: var(--accent-green);
  }
  .letter-body {
    position: absolute; left: 44px; top: 222px; width: 678px;
    font-family: "Arimo", Arial, sans-serif;
    font-size: 13.4px; line-height: 18.6px; letter-spacing: -0.25px;
    color: var(--ink); text-align: justify;
  }
  .letter-body p + p { margin-top: 18.6px; }
  .signature {
    position: absolute; left: 584px; top: 872px;
    width: 116px; height: 84px;
    background: var(--signature-tone); border-radius: 4px;
  }
  .footer-rule {
    position: absolute; left: 0; top: 986px; width: 100%; height: 5px;
    background: var(--accent-green);
  }
  .footer {
    position: absolute; left: 0; top: 996px; width: 100%; height: 92px;
    background: var(--band-grey);
    font-family: "Open Sans", Arial, sans-serif;
    font-size: 11.6px; line-height: 15.5px; color: var(--footer-ink);
  }
  .footer-address { position: absolute; left: 44px; top: 13px; }
  .footer-contacts { position: absolute; left: 256px; top: 9px; list-style: none; }
  .footer-contacts li { display: flex; align-items: center; gap: 8px; height: 16.5px; }
  .footer-contacts svg { width: 10px; height: 10px; flex: none; }
  .footer-registration { position: absolute; left: 530px; top: 42px; }
  .footer-divider {
    position: absolute; top: 12px; width: 1px; height: 44px;
    background: var(--footer-ink);
  }
  .footer-divider.first { left: 209px; }
  .footer-divider.second { left: 499px; }
</style>
</head>
<body>
  <main class="letterhead">
    <div class="top-band"></div>

    <header class="brand">
      <span class="brand-name">Coin Harbour Co</span>
      <span class="brand-dot"></span>
    </header>

    <section class="letter-body">
      <p>Lorem ipsum dolor sit amet, consectetur adipiscing elit. Proin porta, turpis sed elementum semper, est enim viverra nulla, non sollicitudin lorem felis ac enim. Duis varius arcu sed ipsum sollicitudin, vitae consequat ligula rhoncus. Donec blandit quam quis dui lobortis consequat. Vivamus in tempor turpis, sed mollis lacus. Maecenas ac libero erat. Suspendisse elit lacus, bibendum et arcu nec, malesuada vulputate nunc. Nunc enim ex, placerat sit amet porta eu, consequat a risus.</p>
      <p>Lorem ipsum dolor sit amet, consectetur adipiscing elit. Vestibulum pharetra enim at rutrum imperdiet. Aliquam sollicitudin efficitur purus. Integer eros lacus, pellentesque sed ornare eget, imperdiet lacinia est. Sed egestas erat eget erat dictum, et mattis lorem bibendum. Quisque at tellus egestas, finibus augue vel, semper urna. Donec facilisis mi in dui imperdiet, vel aliquet eros hendrerit. Nulla facilisi.</p>
      <p>Nam ipsum purus, pellentesque ac placerat quis, rhoncus quis nisl. Vivamus gravida placerat magna, quis vestibulum odio tincidunt quis. Fusce vitae tristique ipsum. Nam sed velit accumsan quam elementum venenatis. Sed non neque eget felis vulputate condimentum. Nunc ultrices in metus a congue. Maecenas ut erat eget orci feugiat pulvinar quis vitae libero. Sed finibus risus pellentesque libero malesuada hendrerit. Cum sociis natoque penatibus et magnis dis parturient montes, nascetur ridiculus mus. Vestibulum malesuada purus urna, pretium bibendum est iaculis id. Nullam dui arcu, gravida at felis eu, varius venenatis nunc. Sed rutrum pellentesque erat, finibus feugiat nunc porta ac.</p>
      <p>Morbi fringilla malesuada arcu, viverra congue mauris pellentesque sed. Duis elementum faucibus nulla, sit amet sodales lectus scelerisque sed. Pellentesque egestas lorem nulla, vel facilisis urna ultrices ac. Pellentesque ac felis in orci porttitor viverra. Integer tortor nunc, pulvinar id neque nec, convallis rutrum sem. Mauris sed velit erat. Nunc tincidunt, dui ut aliquet consequat, lorem justo accumsan nisi, eget mollis nisl erat non ante. Proin luctus mollis nibh, sit amet placerat mi tempus vel.</p>
      <p>Suspendisse finibus urna sed maximus mollis. Maecenas sit amet suscipit sapien. Donec a justo quis felis pellentesque sodales condimentum non risus. Ut dignissim pellentesque augue, id pharetra odio vulputate eget. Nam non porttitor sapien. Proin iaculis nisi a neque ultrices porta. Curabitur eu congue quam. Lorem ipsum dolor sit amet, consectetur adipiscing elit. Curabitur accumsan at augue ac vestibulum. Sed sed mattis velit. Proin eros risus, viverra nec urna ac, convallis fringilla massa. Pellentesque elementum ligula a sem sollicitudin mattis. Suspendisse eget pretium felis.</p>
    </section>

    <div class="signature" role="img" aria-label="Handwritten signature of the sender"></div>

    <div class="footer-rule"></div>

    <footer class="footer">
      <address class="footer-address" style="font-style:normal">
        Suite 4B Level 17<br>
        Marlowe Crest House<br>
        9 Tindall Lane<br>
        Sydney NSW 2000
      </address>

      <span class="footer-divider first"></span>

      <ul class="footer-contacts">
        <li>
          <svg viewBox="0 0 10 10" aria-hidden="true"><path fill="#fff" d="M2 0.5 3.6 2.6 2.7 3.6Q3.6 5.6 6.4 7.3L7.4 6.4 9.5 8 8.4 9.5Q3.5 8.8 0.5 1.6Z"/></svg>
          <span>02 5193 4620</span>
        </li>
        <li>
          <svg viewBox="0 0 10 10" aria-hidden="true"><rect x="2" y="0.5" width="6" height="9" rx="1" fill="#fff"/><rect x="3" y="1.6" width="4" height="5.6" fill="#7f7f7f"/></svg>
          <span>1300 4719 55</span>
        </li>
        <li>
          <svg viewBox="0 0 10 10" aria-hidden="true"><rect x="0.5" y="0.5" width="9" height="9" rx="2" fill="#fff"/><circle cx="5" cy="5" r="2.2" fill="none" stroke="#7f7f7f" stroke-width="1"/></svg>
          <span>enquiries@coinharbourco.com.au</span>
        </li>
        <li>
          <svg viewBox="0 0 10 10" aria-hidden="true"><circle cx="5" cy="5" r="4.4" fill="#fff"/><path d="M0.8 5H9.2M5 0.8V9.2M2 2.6Q5 4 8 2.6M2 7.4Q5 6 8 7.4" stroke="#7f7f7f" stroke-width="0.7" fill="none"/></svg>
          <span>www.coinharbourco.com.au</span>
        </li>
      </ul>

      <span class="footer-divider second"></span>

      <div class="footer-registration">
        ABN: 47 381 950 623<br>
        ASIC: Registration Number: XXXXXX
      </div>
    </footer>
  </main>
</body>
</html>
```